第3期を迎えるSDGs啓蒙活動である『ハナ凧プロジェクト』のポスターデザインを募集します。
第3期は50社超が参加します。

【作成条件】
・ポスターには参加企業のロゴマークを記載(各社データあり)
・イラスト、写真は問いません
・環境に特化する必要はありません

第2期のポスターデザインを参考にアップしておきますが、卵にはこだわらないで下さい。

今回は参加企業に様々な業種があり、特に金融機関各店舗に掲示するので、高齢の方にも分かりやすいものを選定させて戴きました。
まだまだSDGsの認知も浸透していないので、とにかく分かりやすいという事での選定となりました。

今回は素敵なポスターのご提案に心より感謝申し上げます。
今後も定期的なSDGs勉強会を全国で開催していくので、チラシデザインなどを定期的に発注予定です。
ご縁がございましたら是非ともご提案をお待ちしております。
ありがとうございました。

```html
<!DOCTYPE html>
<html lang="ja">
<head>
<meta charset="utf-8">
<title>HANA DAKO PROJECT — The 3rd period start</title>
<link href="https://fonts.googleapis.com/css2?family=EB+Garamond:wght@400;500&family=Noto+Sans+JP:wght@300;400;500&display=swap" rel="stylesheet">
<style>
  :root{
    --green-deep:#5fb52e;
    --green-mid:#8fcf4a;
    --green-light:#d6edb4;
    --paper:#ffffff;
    --ink:#3a3a3a;
    --ink-soft:#6a6a6a;
    --ball-dark:#2f8f1f;
    --ball-light:#9ee05a;
    --wreath-a:#f2b8a4;
    --wreath-b:#8cc3e8;
    --wreath-c:#f6e27a;
    --wreath-d:#9bcf7a;
  }
  *{margin:0;padding:0;box-sizing:border-box}
  html,body{width:846px;height:1200px;overflow:hidden;background:var(--paper)}
  .poster{
    position:relative;width:846px;height:1200px;overflow:hidden;
    background:linear-gradient(180deg,var(--green-deep) 0%,var(--green-mid) 22%,var(--green-light) 52%,var(--paper) 68%,var(--paper) 100%);
    font-family:"Noto Sans JP",sans-serif;color:var(--ink);
  }
  .title{
    position:absolute;top:26px;left:0;width:100%;text-align:center;
    font-family:"EB Garamond",serif;font-weight:400;color:var(--paper);
    font-size:66px;letter-spacing:1px;line-height:1;
  }
  .subtitle{
    position:absolute;top:118px;left:0;width:100%;text-align:center;
    font-family:"EB Garamond",serif;color:var(--paper);font-size:27px;
  }
  .emblem{position:absolute;left:123px;top:210px;width:600px;height:600px}
  .tagline{
    position:absolute;top:752px;left:0;width:100%;text-align:center;
    font-size:25px;font-weight:300;letter-spacing:4px;color:var(--ink);
  }
  .hosts{
    position:absolute;top:838px;left:30px;right:30px;height:40px;
    display:flex;align-items:center;justify-content:space-between;
    font-size:13px;color:var(--ink);
  }
  .hosts .host{display:flex;align-items:center;gap:5px;font-weight:500}
  .hosts .role{font-size:9px;color:var(--ink-soft);font-weight:400}
  .hosts .mark{width:14px;height:14px;border-radius:50%;background:var(--green-deep)}
  .hosts .badge{width:90px;height:26px;background:#6fbf3a}
  .supporters-label{
    position:absolute;top:890px;left:30px;font-size:9px;letter-spacing:1px;color:var(--ink-soft);
  }
  .supporters{
    position:absolute;top:906px;left:30px;right:30px;
    display:grid;grid-template-columns:repeat(6,1fr);row-gap:6px;column-gap:8px;
  }
  .company{
    display:flex;align-items:center;gap:4px;height:25px;
    font-size:11.5px;font-weight:500;color:var(--ink);white-space:nowrap;overflow:hidden;
  }
  .company .dot{width:8px;height:8px;flex:none;background:var(--green-deep)}
</style>
</head>
<body>
<main class="poster">
  <h1 class="title">HANA DAKO PROJECT</h1>
  <p class="subtitle">The 3rd period start</p>

  <svg class="emblem" viewBox="0 0 600 600" aria-hidden="false">
    <defs>
      <radialGradient id="wreathTone" cx="50%" cy="50%" r="50%">
        <stop offset="62%" stop-color="var(--wreath-d)" stop-opacity="0"/>
        <stop offset="70%" stop-color="var(--wreath-a)"/>
        <stop offset="82%" stop-color="var(--wreath-b)"/>
        <stop offset="92%" stop-color="var(--wreath-c)"/>
        <stop offset="100%" stop-color="var(--wreath-d)" stop-opacity="0"/>
      </radialGradient>
      <radialGradient id="ballTone" cx="40%" cy="35%" r="70%">
        <stop offset="0%" stop-color="var(--ball-light)"/>
        <stop offset="100%" stop-color="var(--ball-dark)"/>
      </radialGradient>
    </defs>
    <circle class="flower-wreath" cx="300" cy="300" r="290" fill="url(#wreathTone)" role="img" aria-label="色とりどりの花と葉で作られたリース"/>
    <circle class="ring" cx="300" cy="300" r="205" fill="var(--paper)"/>
    <circle class="globe" cx="300" cy="300" r="178" fill="url(#ballTone)" role="img" aria-label="緑色に光る地球"/>
    <g class="power-icon" fill="none" stroke="var(--paper)" stroke-width="16" stroke-linecap="round">
      <path d="M250 245 A82 82 0 1 0 350 245"/>
      <line x1="300" y1="200" x2="300" y2="300"/>
    </g>
  </svg>

  <p class="tagline">いくつもの花、咲かせます</p>

  <section class="hosts">
    <div class="host"><span class="role">主催</span><span class="mark"></span>けやき市</div>
    <div class="host"><span class="role">共催</span>ひろば財団</div>
    <div class="host"><span class="role">後援</span>あおば新聞</div>
    <div class="host"><span class="role">協力</span>ゆめ信用金庫</div>
    <div class="host">地域SDGs推進会議</div>
    <div class="badge"></div>
  </section>

  <p class="supporters-label">SUPPORTING COMPANY</p>
  <section class="supporters">
    <div class="company"><span class="dot"></span>みどり銀行</div>
    <div class="company"><span class="dot"></span>青葉建設</div>
    <div class="company"><span class="dot"></span>さくら信金</div>
    <div class="company"><span class="dot"></span>ひかり電機</div>
    <div class="company"><span class="dot"></span>若草運輸</div>
    <div class="company"><span class="dot"></span>大空食品</div>
    <div class="company"><span class="dot"></span>森野商事</div>
    <div class="company"><span class="dot"></span>川辺工業</div>
    <div class="company"><span class="dot"></span>朝日印刷</div>
    <div class="company"><span class="dot"></span>つばさ保険</div>
    <div class="company"><span class="dot"></span>花見証券</div>
    <div class="company"><span class="dot"></span>しずく水道</div>
    <div class="company"><span class="dot"></span>山吹製作所</div>
    <div class="company"><span class="dot"></span>こもれび住宅</div>
    <div class="company"><span class="dot"></span>白鷺物流</div>
    <div class="company"><span class="dot"></span>すずらん薬局</div>
    <div class="company"><span class="dot"></span>陽だまり不動産</div>
    <div class="company"><span class="dot"></span>星野化学</div>
    <div class="company"><span class="dot"></span>あおい信用組合</div>
    <div class="company"><span class="dot"></span>風見エネルギー</div>
    <div class="company"><span class="dot"></span>月光ホテル</div>
    <div class="company"><span class="dot"></span>野ばら農園</div>
    <div class="company"><span class="dot"></span>はやて交通</div>
    <div class="company"><span class="dot"></span>いずみ酒造</div>
    <div class="company"><span class="dot"></span>東雲リース</div>
    <div class="company"><span class="dot"></span>みなと電設</div>
    <div class="company"><span class="dot"></span>若葉ガス</div>
    <div class="company"><span class="dot"></span>ことり書房</div>
    <div class="company"><span class="dot"></span>松風製菓</div>
    <div class="company"><span class="dot"></span>ひまわり介護</div>
    <div class="company"><span class="dot"></span>たけのこ設計</div>
    <div class="company"><span class="dot"></span>虹色通信</div>
    <div class="company"><span class="dot"></span>こがね精機</div>
    <div class="company"><span class="dot"></span>あかね病院</div>
    <div class="company"><span class="dot"></span>千草フーズ</div>
    <div class="company"><span class="dot"></span>うみべ観光</div>
    <div class="company"><span class="dot"></span>くすのき会計</div>
    <div class="company"><span class="dot"></span>なぎさ塗装</div>
    <div class="company"><span class="dot"></span>杉並木材</div>
    <div class="company"><span class="dot"></span>ゆうひ放送</div>
    <div class="company"><span class="dot"></span>はなみずき歯科</div>
    <div class="company"><span class="dot"></span>木の実ベーカリー</div>
    <div class="company"><span class="dot"></span>白樺システム</div>
    <div class="company"><span class="dot"></span>ほたる照明</div>
    <div class="company"><span class="dot"></span>北斗鉄工</div>
    <div class="company"><span class="dot"></span>さざなみ水産</div>
    <div class="company"><span class="dot"></span>紅葉クリーニング</div>
    <div class="company"><span class="dot"></span>あさぎ商会</div>
    <div class="company"><span class="dot"></span>そよ風空調</div>
    <div class="company"><span class="dot"></span>いちょう銀行</div>
    <div class="company"><span class="dot"></span>かすみ技研</div>
    <div class="company"><span class="dot"></span>とんぼ文具</div>
    <div class="company"><span class="dot"></span>ひばり保育</div>
    <div class="company"><span class="dot"></span>みずかね電工</div>
  </section>
</main>
</body>
</html>
```